5 Blog Posts and Lead Magnet Needs Branding for Remodeling Company

I have 5 blogs and a website lead magnet that have content written but need some design and layout help to align with my brand identity. The content will need to be formatted for social media and website. I have a logo, colors and font. I also have a website I'm pretty happy with right now that can provide direction.
Target Market(s)
Age 40-65, Average salary 250K, Male/Female Professional College + Married 3 + Mid-full size car with high end finishes.
Industry/Entity Type
Construction, remodeling
Colors
Look and feel

```html
<!DOCTYPE html>
<html lang="en">
<head>
<meta charset="utf-8">
<title>5 Mistakes People Make When Planning a Major Home Remodel</title>
<link rel="stylesheet" href="https://fonts.googleapis.com/css2?family=Montserrat:wght@400;500;700;800;900&display=swap">
<style>
  :root {
    --navy: #0e1a4d;
    --gold: #c8a46e;
    --slate: #6b7290;
    --paper: #f3f4f6;
    --white: #ffffff;
    --ink: #141c3f;
  }
  * { margin: 0; padding: 0; box-sizing: border-box; }
  html, body { width: 1200px; height: 582px; overflow: hidden; background: var(--navy); }
  body { font-family: "Montserrat", sans-serif; color: var(--ink); position: relative; }

  .page {
    position: absolute; top: 26px; width: 373px; height: 527px;
    background: linear-gradient(90deg, var(--paper) 0 144px, var(--white) 144px 100%);
    overflow: hidden;
  }
  .page--cover { left: 27px; background: var(--paper); }
  .page--one { left: 415px; }
  .page--two { left: 802px; }

  /* Cover */
  .brand { position: absolute; left: 25px; top: 32px; width: 70px; text-align: center; }
  .brand__name { font-weight: 800; font-size: 17px; line-height: 1; color: var(--navy); letter-spacing: -0.3px; }
  .brand__tag { margin-top: 4px; font-weight: 800; font-size: 4px; letter-spacing: 0.2px; color: var(--navy); border-top: 0.6px solid var(--navy); padding-top: 2px; }
  .cover__number {
    position: absolute; left: 20px; top: 178px; font-weight: 900; font-size: 236px;
    line-height: 1; color: var(--gold); letter-spacing: -6px;
  }
  .cover__title {
    position: absolute; left: 25px; top: 385px; font-weight: 900; font-size: 29.5px;
    letter-spacing: -1.2px; color: var(--navy); line-height: 1;
  }
  .cover__sub { position: absolute; left: 27px; top: 420px; width: 138px; color: var(--navy); }
  .cover__sub span { display: block; font-size: 13px; line-height: 12.6px; text-align: justify; text-align-last: justify; font-weight: 500; }
  .cover__sub strong { display: block; font-size: 15.6px; font-weight: 800; line-height: 15px; letter-spacing: -0.4px; }
  .cover__band {
    position: absolute; left: 0; top: 471px; width: 164px; height: 24px; background: var(--gold);
    color: var(--white); font-weight: 800; font-size: 9.6px; letter-spacing: -0.3px;
    line-height: 24px; padding-left: 26px;
  }
  .cover__photo {
    position: absolute; left: 190px; top: 31px; width: 151px; height: 465px;
    background: linear-gradient(180deg, #e7e6e3 0%, #cfcac4 35%, #8fa9c9 65%, #c9cdd3 100%);
  }

  /* Mistake pages */
  .mistake__label {
    position: absolute; left: 26px; top: 24px; width: 100px; text-align: right;
    font-weight: 900; font-size: 25px; letter-spacing: -1.3px; color: var(--navy); line-height: 1;
  }
  .mistake__label b { display: block; font-size: 46px; color: var(--gold); line-height: 0.95; letter-spacing: 0; }
  .mistake__heading {
    position: absolute; left: 161px; top: 26px; width: 200px;
    font-weight: 900; font-size: 15.4px; line-height: 14.6px; letter-spacing: -0.3px; color: var(--slate);
  }
  .copy { position: absolute; left: 76px; width: 268px; font-size: 7.1px; line-height: 9.05px; letter-spacing: -0.08px; }
  .copy p { margin-bottom: 9px; text-align: justify; hyphens: auto; }
  .copy p.left { text-align: left; }
  .copy strong { font-weight: 700; color: var(--navy); }
  .photo { position: absolute; }
  .photo--money { left: 76px; top: 245px; width: 268px; height: 90px;
    background: linear-gradient(160deg, #f8d858 0%, #f5d24f 55%, #e9e5dc 100%); }
  .photo--team { top: 242px; width: 131px; height: 59px;
    background: linear-gradient(120deg, #9fb4cf 0%, #d9dde3 55%, #b8c3cf 100%); }
  .photo--team-a { left: 76px; }
  .photo--team-b { left: 213px; }
</style>
</head>
<body>

<section class="page page--cover">
  <div class="brand">
    <div class="brand__name">Halden</div>
    <div class="brand__tag">HOME IMPROVEMENTS</div>
  </div>
  <div class="cover__number">5</div>
  <h1 class="cover__title">MISTAKES</h1>
  <div class="cover__sub">
    <span>PEOPLE MAKE WHEN</span>
    <span>PLANNING A MAJOR</span>
    <strong>HOME REMODEL</strong>
  </div>
  <div class="cover__band">AND HOW TO AVOID THEM</div>
  <div class="cover__photo" role="img" aria-label="Photo of a smiling couple in a kitchen looking at a laptop together"></div>
</section>

<section class="page page--one">
  <div class="mistake__label">MISTAKE<b>1</b></div>
  <h2 class="mistake__heading">NOT PLANNING YOUR BUDGET.</h2>
  <div class="copy" style="top:102px">
    <p class="left">Before you speak to anybody, you need to know your budget. Know what you can afford and what you would like to spend.</p>
    <p class="left">Keep in mind that these two numbers are never the same, so decide on your limit for the redesign &amp; construction of your existing home.</p>
    <p class="left">Once you have decided on a budget, it's in your best interest to share this information with everyone involved in the design process.</p>
    <p><strong>The single biggest mistake consumers make when remodeling their home is when they either understate their budget or refuse to set one.</strong></p>
    <p>A professional will make sure they design your home to suit your lifestyle and fit in with your budget. Contrary to popular belief, you will not pay more for a home just because you disclose a larger budget.</p>
  </div>
  <div class="photo photo--money" role="img" aria-label="Photo of a calculator, dollar bills, keyboard and notebook on a yellow desk"></div>
  <div class="copy" style="top:345px">
    <p><strong>You are not negotiating the price at this stage of the process!</strong></p>
    <p>By discussing your budget openly with the designer at the beginning of the project, you'll be able to find out if what you're after is achievable. If it's not and the size of the remodel is not within your budget, a professional designer can make recommendations on where to cut back based on your priorities.</p>
    <p>It's important to establish the fundamentals before the design work commences otherwise you will find yourself constantly redesigning your home and struggling to hit the target budget.</p>
    <p>If you are in the fortunate position of not being restricted by a limited budget the design brief should focus on lifestyle and quality of finishes. However, if budget is your #1 priority, capping the overall size of the remodel along with the architectural flare of the design will be important aspects to take control of early.</p>
  </div>
</section>

<section class="page page--two">
  <div class="mistake__label">MISTAKE<b>2</b></div>
  <h2 class="mistake__heading">NOT PLANNING YOUR REMODELING TEAM.</h2>
  <div class="copy" style="top:102px">
    <p class="left">It may surprise you to learn that over 80% of designs never get built.</p>
    <p class="left">Why? They came in <strong>way over budget</strong>.</p>
    <p>The reason for this is simple. Architects design major remodels that meet a consumer's brief rather than their budget.</p>
    <p>While budgets are generally discussed with architects at the briefing stage, building designers and architects have little knowledge of building costs and generally underestimate the cost to complete a major remodel by 50-300%. That is a huge amount of money for you to find which is why these designs never see the light of day.</p>
    <p>The solution to this problem is quite simple, involve your builder at the design stage.</p>
  </div>
  <div class="photo photo--team photo--team-a" role="img" aria-label="Photo of a team reviewing building plans at a table"></div>
  <div class="photo photo--team photo--team-b" role="img" aria-label="Photo of three colleagues leaning over architectural drawings in an office"></div>
  <div class="copy" style="top:336px">
    <p>By involving a builder at the design stage, you can design your home's new look to be both practical and within your budget.</p>
    <p>Only a professional &amp; custom remodeling specialist has the experience to foresee the potential cost implications of a difficult site or architectural features.</p>
    <p>Whilst you may be paying $10,000-$50,000 for an architect to design the remodel, most professional builders will consult on a project for as little as a few thousand dollars. Most remodeling specialists provide a design and build service which means the consultation service is generally included free of charge.</p>
    <p>A professional will also have the right team in place to handle the more complex side of your project. It often takes a team including your builder, their designer, certifier and town planner to scope out legal requirements and any permits required to make sure what you want can actually be built.</p>
    <p>Getting your design and specifications right in the beginning will save you thousands of dollars in potential redesign fees and months of wasted time.</p>
  </div>
</section>

</body>
</html>
```